Architecture firm needing a business card

We need a business card design for a new company based in the US called "Pellmore Architecture". Seeking minimalist designs that have a creativity/design feel but must be clean and professional. Please refer to the logo attached.

Target Market(s)

Real Estate Investors, Home Builders and Construction Firms.

Industry/Entity Type

Architecture

Contact Information for Business Card

Standard US size business cards. Would like to have some sort of graphic on the back side of the card - nothing that is too loud but something that may catch your attention. More or less grayscale colors that are in line with the logo colors (navy and greys essentially). Additional colors maybe accepted if blended properly (earthtones), but might be difficult to accomplish and maintain the clean/minimalist look.

Requirements
Must have
• Clean Lines
Nice to have
• some sort of graphics, would like to have something creative on the back side of the card
Should not have
• nothing too busy, cluttered or overwhelming.

```html
<!DOCTYPE html>
<html lang="en">
<head>
<meta charset="utf-8">
<title>Pellmore Architecture — Business Card</title>
<link rel="stylesheet" href="https://fonts.googleapis.com/css2?family=Jost:wght@400;500&display=swap">
<style>
  :root {
    --navy: #1f4774;
    --navy-deep: #1a3d66;
    --grey: #9a9a9a;
    --text-grey: #6b6b6b;
    --paper: #f7f7f7;
    --stage: #3b3b3b;
  }
  * { box-sizing: border-box; margin: 0; padding: 0; }
  html, body { width: 1200px; height: 768px; overflow: hidden; }
  body {
    background: var(--stage);
    font-family: "Jost", "Futura", sans-serif;
    display: flex;
    align-items: center;
    justify-content: center;
    gap: 40px;
  }
  .card {
    position: relative;
    width: 520px;
    height: 297px;
    overflow: hidden;
  }

  /* Back side */
  .card-back { background: var(--navy); }
  .back-pattern {
    position: absolute; inset: 0;
    background: linear-gradient(135deg, #24507f 0%, var(--navy-deep) 100%);
  }
  .back-brand {
    position: absolute; right: 34px; bottom: 34px;
    display: flex; flex-direction: column; align-items: flex-end; gap: 8px;
  }
  .back-brand .mark-square {
    width: 46px; height: 46px; border: 3px solid #e6e9ee;
  }
  .back-brand .web {
    font-size: 12px; color: #dfe4ea; letter-spacing: 0.04em;
  }

  /* Front side */
  .card-front { background: var(--paper); color: var(--text-grey); }
  .side-band {
    position: absolute; left: 0; top: 0; bottom: 0; width: 34px;
    background: var(--navy);
  }
  .side-band::before {
    content: ""; position: absolute; left: 0; top: 0; width: 100%; height: 78px;
    background: var(--grey);
  }
  .brand {
    position: absolute; left: 64px; top: 36px;
    display: flex; align-items: center; gap: 12px;
  }
  .brand .mark-square { width: 30px; height: 30px; background: var(--navy); }
  .brand .name {
    font-size: 27px; font-weight: 400; color: var(--navy);
    letter-spacing: 0.06em; text-transform: uppercase;
  }
  .person { position: absolute; left: 64px; top: 116px; }
  .person .full-name { font-size: 18px; font-weight: 500; color: var(--navy); }
  .person .role { font-size: 12px; color: var(--text-grey); margin-top: 1px; }
  .rule {
    position: absolute; left: 136px; right: 28px; top: 153px;
    height: 1px; background: var(--navy);
  }
  .contacts {
    position: absolute; left: 64px; top: 166px;
    list-style: none; font-size: 12.5px; line-height: 19px;
  }
  .contacts li { display: flex; align-items: center; gap: 8px; }
  .contacts svg { width: 11px; height: 11px; fill: var(--navy); flex: none; }
  .address {
    position: absolute; right: 40px; bottom: 30px;
    font-size: 12.5px; line-height: 17px; text-align: left;
  }
</style>
</head>
<body>

  <section class="card card-back" aria-label="Card back">
    <div class="back-pattern" role="img" aria-label="Repeating geometric brand pattern in tonal navy"></div>
    <div class="back-brand">
      <div class="mark-square"></div>
      <span class="web">www.pellmorestudio.com</span>
    </div>
  </section>

  <section class="card card-front" aria-label="Card front">
    <div class="side-band"></div>

    <div class="brand">
      <div class="mark-square"></div>
      <span class="name">Pellmore Architecture</span>
    </div>

    <div class="person">
      <p class="full-name">Daniel Reyes</p>
      <p class="role">CEO/Founder</p>
    </div>
    <div class="rule"></div>

    <ul class="contacts">
      <li>
        <svg viewBox="0 0 12 12" aria-hidden="true"><path d="M2.3 0.8 4 2.5 3.2 4.2c.8 1.7 2 2.9 3.6 3.6l1.6-.8 1.8 1.8-1 1.6C5.4 10.2 1.8 6.6 1 2.8z"/></svg>
        208 514 7720
      </li>
      <li>
        <svg viewBox="0 0 12 12" aria-hidden="true"><path d="M3 0h6v12H3zM4 1.5v8h4v-8zM5.5 10.2h1v1h-1z" fill-rule="evenodd"/></svg>
        208 639 4185
      </li>
      <li>
        <svg viewBox="0 0 12 12" aria-hidden="true"><path d="M3 0h5l1 1v3H3zM0 5h12v5H9v2H3v-2H0zM4 8v3h4V8z" fill-rule="evenodd"/></svg>
        208 772 3056
      </li>
      <li>
        <svg viewBox="0 0 12 12" aria-hidden="true"><path d="M0 2h12v8H0zM1 3l5 4 5-4z" fill-rule="evenodd"/></svg>
        hello@pellmorestudio.com
      </li>
    </ul>

    <address class="address" style="font-style: normal;">
      4120 Larkspur Court<br>
      Boise, Idaho 83702<br>
      www.pellmorestudio.com
    </address>
  </section>

</body>
</html>
```